" A empresa funciona em um escritório físico, onde os clientes são recebidos para conversar sobre como desejam seu projeto residencial ou comercial. Oferecemos também projetos de decoração, e de instalações, bem como projeto de estrutura. O processo de criação se da tambem pela produção de projetos em 3d. alem da produção do projeto acompanhamos tambem a obra e todo o processo de construção. "

```html
<!DOCTYPE html>
<html lang="pt-BR">
<head>
<meta charset="UTF-8">
<title>Marisa Tavares — Pasta Institucional</title>
<link href="https://fonts.googleapis.com/css2?family=Montserrat:wght@300;400;500&display=swap" rel="stylesheet">
<style>
  :root {
    --backdrop: #e4e2df;
    --paper: #ffffff;
    --fold-shade: #c9c9cb;
    --slate: #6b6b6d;
    --slate-light: #8a8a8c;
    --sun: #fdd922;
    --ink-soft: #7a7a7c;
  }
  * { margin: 0; padding: 0; box-sizing: border-box; }
  html, body {
    width: 1200px; height: 1200px; overflow: hidden;
    background: var(--backdrop);
    font-family: "Montserrat", sans-serif;
  }
  .folder {
    position: absolute; left: 53px; top: 106px;
    width: 1094px; height: 980px;
  }
  .panel-inner {
    position: absolute; left: 0; top: 0; width: 547px; height: 100%;
    background: linear-gradient(90deg, var(--paper) 0%, var(--paper) 62%, var(--fold-shade) 100%);
  }
  .panel-cover {
    position: absolute; left: 547px; top: 0; width: 547px; height: 100%;
    background: var(--slate);
  }
  .brand-field {
    position: absolute; left: 43px; top: 182px;
  }
  .contact {
    position: absolute; left: 53px; top: 686px;
    font-size: 9.5px; line-height: 14px; color: var(--ink-soft);
    list-style: none;
  }
  .contact li::before {
    content: ""; display: inline-block; width: 5px; height: 5px;
    border-radius: 50%; background: var(--sun);
    margin-right: 7px; vertical-align: middle;
  }
  .pocket {
    position: absolute; left: -30px; top: 858px;
  }
  .cover-identity {
    position: absolute; left: 547px; top: 360px; width: 547px;
    text-align: center; color: var(--paper);
  }
  .brand-name {
    display: inline-flex; align-items: center; gap: 12px;
    font-size: 25px; font-weight: 300; letter-spacing: 2px;
    text-transform: uppercase;
  }
  .brand-dot {
    width: 18px; height: 18px; border-radius: 50%; background: var(--sun);
  }
  .brand-tagline {
    margin-top: 6px; font-size: 10px; font-weight: 400;
    letter-spacing: 2.5px; color: var(--sun); text-transform: uppercase;
  }
  .cover-bar {
    position: absolute; left: 746px; top: 758px;
    width: 161px; height: 14px; background: var(--sun);
  }
</style>
</head>
<body>
  <div class="folder">
    <section class="panel-inner">
      <svg class="brand-field" width="590" height="480" viewBox="0 0 590 480" role="img" aria-label="Large brand symbol decoration in yellow and grey">
        <defs>
          <linearGradient id="field-tone" x1="0" y1="0" x2="1" y2="0">
            <stop offset="0" stop-color="#fdd922"/>
            <stop offset="0.5" stop-color="#e8d56a"/>
            <stop offset="1" stop-color="#8a8a8c"/>
          </linearGradient>
        </defs>
        <rect x="0" y="0" width="590" height="480" rx="40" fill="url(#field-tone)" opacity="0.9"/>
      </svg>
      <ul class="contact">
        <li>Pç. Rui Campos Lemos 210 sala 4</li>
        <li>Centro • Vale Alto • Bahia</li>
        <li>(71) 5555-2140 - 95550-3182</li>
        <li>contato@marisatavares.com</li>
      </ul>
      <svg class="pocket" width="600" height="130" viewBox="0 0 600 130">
        <path d="M0 6 L70 0 L70 18 L500 18 Q560 18 580 60 Q596 100 577 126 L60 126 L60 110 L8 104 Z" fill="var(--sun)"/>
        <path d="M70 18 L70 126" stroke="#e3c312" stroke-width="2"/>
      </svg>
    </section>
    <section class="panel-cover">
    </section>
    <div class="cover-identity">
      <div class="brand-name"><span class="brand-dot"></span>Marisa Tavares</div>
      <p class="brand-tagline">Arquitetura • Interiores</p>
    </div>
    <div class="cover-bar"></div>
  </div>
</body>
</html>
```